English and Spanish Language School Needs a Business Card

Need a business card design a startup company called Corvelle Language School. The company will offer English and Spanish conversational level courses designed to make the learner feel comfortable with grammar and vocabulary. We would like to see a logo with some colour that should communicate learning, growth.

Target Market(s)

Consumers and businesses

Industry/Entity Type

Education

Contact Information for Business Card

TBD

Font styles to use
Serif

Requirements
Must have
• Include the following
• Logo
• Name
• Title
• Cellphone Number
• Office Phone number
• Email address
• Office Address

```html
<!DOCTYPE html>
<html lang="en">
<head>
<meta charset="utf-8">
<title>Corvelle Language School – Business Card</title>
<link href="https://fonts.googleapis.com/css2?family=Tinos:wght@400;700&display=swap" rel="stylesheet">
<style>
  :root {
    --card-white: #f7f7f7;
    --brand-red: #d0222f;
    --brand-red-dark: #b51b27;
    --brand-teal: #16b3b8;
    --text-light: #ffffff;
    --stage: #e6e3de;
  }
  * { margin: 0; padding: 0; box-sizing: border-box; }
  html, body {
    width: 1200px; height: 780px; overflow: hidden;
    background: var(--stage);
    font-family: "Tinos", "Times New Roman", serif;
  }
  .canvas { position: relative; width: 1200px; height: 780px; }
  .card {
    position: absolute; top: 240px;
    width: 520px; height: 300px;
    border-radius: 14px; overflow: hidden;
    background: var(--card-white);
    box-shadow: 0 10px 28px rgba(0,0,0,.18);
  }
  .card--front { left: 45px; }
  .card--back { left: 635px; }
  .card-art { position: absolute; inset: 0; }

  .brand { position: absolute; color: var(--brand-red); font-weight: 700; line-height: 1; }
  .brand-dot {
    display: inline-block; width: 14px; height: 14px; border-radius: 50%;
    background: var(--brand-teal); margin-left: 8px; vertical-align: middle;
  }
  .brand-name { font-size: 46px; letter-spacing: -0.5px; }
  .brand-sub { font-size: 19px; margin-top: 6px; letter-spacing: .3px; }
  .card--front .brand { left: 30px; top: 40px; }
  .card--back .brand { right: 40px; top: 100px; text-align: right; }
  .card--back .brand-name { font-size: 56px; }
  .card--back .brand-sub { font-size: 22px; }

  .person { position: absolute; left: 36px; top: 206px; color: var(--text-light); text-align: right; width: 170px; }
  .person-name { font-size: 20px; font-weight: 700; letter-spacing: .5px; }
  .person-title { font-size: 14px; margin-top: 2px; }
  .divider { position: absolute; left: 222px; top: 196px; width: 1px; height: 56px; background: rgba(255,255,255,.55); }
  .contacts { position: absolute; left: 238px; top: 168px; list-style: none; color: var(--text-light); font-size: 14px; line-height: 1.55; }
  .contacts li { display: flex; align-items: center; gap: 8px; }
  .contacts svg { width: 12px; height: 12px; fill: var(--text-light); flex: none; }
  .address {
    position: absolute; left: 0; right: 0; bottom: 0; height: 36px;
    display: flex; align-items: center; justify-content: center;
    color: var(--text-light); font-size: 15px; letter-spacing: .3px;
  }
</style>
</head>
<body>
<main class="canvas">

  <section class="card card--front" aria-label="Business card front">
    <svg class="card-art" viewBox="0 0 520 300" aria-hidden="true">
      <path d="M338,0 C318,108 205,168 0,186" fill="none" stroke="var(--brand-teal)" stroke-width="5"/>
      <path d="M352,0 C332,118 215,180 0,196 L0,300 L520,300 L520,0 Z" fill="var(--brand-red)"/>
      <rect x="0" y="264" width="520" height="36" fill="var(--brand-teal)"/>
    </svg>
    <div class="brand">
      <div class="brand-name">Corvelle<span class="brand-dot"></span></div>
      <div class="brand-sub">Language School</div>
    </div>
    <div class="person">
      <div class="person-name">DANIEL MARSH</div>
      <div class="person-title">Manager</div>
    </div>
    <span class="divider"></span>
    <ul class="contacts">
      <li><svg viewBox="0 0 12 12"><rect x="3" y="0" width="6" height="12" rx="1.2"/></svg>123 456 7890</li>
      <li><svg viewBox="0 0 12 12"><path d="M1 4 Q6 0 11 4 L9 5.5 L8 4 Q6 3 4 4 L3 5.5Z M2 7 H10 V11 H2Z"/></svg>123 456 7890</li>
      <li><svg viewBox="0 0 12 12"><path d="M0 2 H12 V10 H0Z M1 3 L6 7 L11 3" stroke="var(--brand-red)" stroke-width="1"/></svg>hello@corvelleschool.com</li>
    </ul>
    <div class="address">Your Address, 2nd Ste Alder Bend, Texas 1234</div>
  </section>

  <section class="card card--back" aria-label="Business card back">
    <svg class="card-art" viewBox="0 0 520 300" aria-hidden="true">
      <path d="M0,0 L118,0 C70,90 80,210 180,300 L0,300 Z" fill="var(--brand-red)"/>
      <path d="M128,0 C80,90 90,210 192,300" fill="none" stroke="var(--brand-teal)" stroke-width="5"/>
    </svg>
    <div class="brand">
      <div class="brand-name">Corvelle<span class="brand-dot"></span></div>
      <div class="brand-sub">Language School</div>
    </div>
  </section>

</main>
</body>
</html>
```